Flyer-Design für Händler von Premium-Olivenöl
Zielgruppe
Wir vertreiben Premium Olivenöl.
Aufgabenstellung
Gerne Anlehnung an unsere Homepage: www.lunadoru.de
Hier stehen sämtliche Informationen zur Verfügung.
Unser Werbeträger Lukas Brandt sollte gut sichtbar auf dem Flyer sein.
Gerne schicken wir dann per Mail weitere Fotos.

```html
<!DOCTYPE html>
<html lang="de">
<head>
<meta charset="utf-8">
<title>luna doru – Flyer</title>
<link rel="stylesheet" href="https://fonts.googleapis.com/css2?family=Crimson+Pro:wght@400;600&display=swap">
<style>
  :root{
    --stage:#b8b7b2;
    --paper:#f4f5f3;
    --paper-shade:#ebecea;
    --ink:#2b2b2b;
    --green:#7aa547;
    --green-dark:#5f8a34;
    --band-text:#ffffff;
  }
  *{box-sizing:border-box;margin:0;padding:0}
  html,body{width:1076px;height:1200px;overflow:hidden}
  body{background:var(--stage);font-family:"Crimson Pro",Georgia,serif;color:var(--ink);position:relative}
  .flyer{position:absolute;left:223px;width:630px;height:500px;display:flex;box-shadow:0 14px 30px rgba(0,0,0,.18)}
  .flyer--outside{top:45px}
  .flyer--inside{top:640px}
  .panel{position:relative;width:210px;height:100%;background:var(--paper);overflow:hidden}
  .panel--middle{background:var(--paper-shade)}
  .rule{position:absolute;left:0;right:0;height:4px;background:var(--green)}
  .photo{position:absolute;box-shadow:inset 0 0 0 1px rgba(0,0,0,.06)}
  .brand{position:absolute;left:0;right:0;text-align:center}
  .brand__mark{width:56px;height:56px;border-radius:50%;border:2px solid var(--ink);margin:0 auto 8px}
  .brand__name{font-size:26px;font-weight:600;line-height:1;letter-spacing:.5px}
  .brand__tag{font-size:10px;letter-spacing:1.5px;margin-top:4px;color:var(--green-dark)}
  .intro{position:absolute;top:24px;left:16px;right:16px;font-size:13.5px;line-height:1.35;font-weight:600}
  .copy{font-size:11px;line-height:1.4}
  .heading{font-size:12px;font-weight:600;text-decoration:underline;text-decoration-color:var(--green);text-underline-offset:2px;margin-bottom:8px}
  .contact{position:absolute;top:148px;left:0;right:0;text-align:center;font-size:10.5px;line-height:1.35}
  .claim{position:absolute;top:156px;left:18px;right:18px;text-align:center;color:var(--green);font-size:12.5px;line-height:1.3}
  .band{position:absolute;left:0;right:0;bottom:0;height:46px;background:var(--green);color:var(--band-text);font-size:12px;display:flex;align-items:center;justify-content:center}
  .olive-icon{position:absolute;right:24px;top:150px}
</style>
</head>
<body>

<section class="flyer flyer--outside">
  <div class="panel">
    <p class="intro">olivenöl aus sonnigen hainen, kalt gepresst und sorgsam abgefüllt für den feinsten geschmack</p>
    <div class="rule" style="top:190px"></div>
    <div class="photo" role="img" aria-label="Foto: Werbeträger Lukas Brandt lächelnd am Gartentisch mit einer Flasche luna doru Olivenöl" style="top:194px;left:0;right:0;bottom:0;background:linear-gradient(165deg,#a08a66 0%,#7e8a5c 30%,#5b6480 58%,#3c4766 80%,#8a6f4f 100%)"></div>
  </div>
  <div class="panel panel--middle">
    <div class="brand" style="top:24px">
      <div class="brand__mark"></div>
      <div class="brand__name" style="font-size:16px">luna doru</div>
    </div>
    <p class="contact">luna doru gmbh<br>inhaber<br>lindenweg 12<br>80331 münchen<br>+49 89 000000</p>
    <div class="photo" role="img" aria-label="Schwarz-Weiß-Foto: Lukas Brandt und ein Freund lachend nebeneinander" style="top:222px;left:26px;right:26px;height:250px;background:linear-gradient(180deg,#d8d8d6 0%,#a9a9a7 30%,#5e5e5e 65%,#2f2f2f 100%)"></div>
  </div>
  <div class="panel">
    <div class="brand" style="top:22px">
      <div class="brand__mark"></div>
      <div class="brand__name">luna doru</div>
      <div class="brand__tag">feinstes olivenöl</div>
    </div>
    <div class="rule" style="top:152px"></div>
    <div class="photo" role="img" aria-label="Foto: eine weiße und eine schwarze Olivenölflasche mit Brot und einer Schale Öl" style="top:156px;left:0;right:0;bottom:0;background:linear-gradient(170deg,#e4e1da 0%,#c7ab7e 35%,#3a3a36 55%,#c9a64a 78%,#ece9e2 100%)"></div>
  </div>
</section>

<section class="flyer flyer--inside">
  <div class="panel">
    <div style="position:absolute;top:20px;left:16px;right:16px">
      <p class="heading">olivenöl – hergestellt aus liebe</p>
      <p class="copy">unsere oliven wachsen auf kleinen familiengütern und werden von hand geerntet, damit jede flasche ihren vollen charakter behält.</p>
    </div>
    <svg class="olive-icon" width="26" height="30" viewBox="0 0 26 30" aria-hidden="true">
      <circle cx="13" cy="18" r="11" fill="var(--green)"/>
      <path d="M13 7 Q16 1 22 2 Q19 7 13 7Z" fill="var(--green-dark)"/>
    </svg>
    <div style="position:absolute;top:205px;left:16px;right:16px">
      <p class="heading">schonende pressung für reinen genuss</p>
      <p class="copy">kalt gepresst wenige stunden nach der ernte, ohne zusätze und ohne kompromisse.</p>
    </div>
    <div class="photo" role="img" aria-label="Foto: Olivenölflasche mit Brot und Kräutern auf einem Holzbrett" style="top:330px;left:16px;right:16px;height:108px;background:linear-gradient(150deg,#d6c7a8,#8d7252 45%,#2f2f2f 75%,#6b6b66)"></div>
    <div class="band">herkunft</div>
  </div>
  <div class="panel panel--middle">
    <div class="brand" style="top:20px">
      <div class="brand__mark"></div>
      <div class="brand__name">luna doru</div>
      <div class="brand__tag">feinstes olivenöl</div>
    </div>
    <p class="claim">luna doru steht für echten genuss, ehrliche herkunft und feinsten geschmack.</p>
    <div class="photo" role="img" aria-label="Foto: Olivenölflasche auf einem Tisch, Hände beim gemeinsamen Essen" style="top:300px;left:16px;right:16px;height:138px;background:linear-gradient(160deg,#ebe9e4,#b39f82 45%,#3a3f4c 75%,#9a8a73)"></div>
    <div class="band">beste qualität</div>
  </div>
  <div class="panel">
    <div style="position:absolute;top:20px;left:16px;right:16px">
      <p class="heading">luna doru – unser versprechen</p>
      <p class="copy" style="margin-bottom:12px">gemeinsam mit kleinen erzeugern wählen wir nur die besten oliven aus. jede charge wird geprüft, bevor sie in unsere flaschen kommt und ihren weg zu ihnen findet.</p>
      <p class="copy">lukas brandt schätzt unser öl in der täglichen küche – pur, zum brot oder für den salat.</p>
    </div>
    <div class="photo" role="img" aria-label="Foto: Hand tunkt Brot in eine Schale Olivenöl" style="top:330px;left:16px;right:16px;height:76px;background:linear-gradient(170deg,#efeeea,#b7b2a8 55%,#7d838c)"></div>
    <div class="band">flüssiges gold</div>
  </div>
</section>

</body>
</html>
```